Powerpoint Slide Deck

I had my logo designed using artfolda and would like to have a professional looking powerpoint deck created with my logo etc. my website is brovana.info

```html
<!DOCTYPE html>
<html lang="en">
<head>
<meta charset="utf-8">
<title>Brovana – Presentation Deck</title>
<link href="https://fonts.googleapis.com/css2?family=Lexend:wght@400;500&family=Roboto:wght@400;500;700&display=swap" rel="stylesheet">
<style>
:root{
  --page:#edf2f2;
  --dark:#2c3536;
  --green:#3e9c78;
  --orange:#dd6a1d;
  --blue:#1f7fcf;
  --text:#4a4f52;
  --white:#ffffff;
}
*{box-sizing:border-box;margin:0;padding:0}
html,body{width:1200px;height:4051px;overflow:hidden;background:var(--page)}
body{position:relative;font-family:'Roboto',sans-serif;color:var(--text)}
.slide{position:absolute;left:75px;width:1048px;height:588px;background:var(--white);border-bottom:5px solid var(--blue);box-shadow:0 6px 18px rgba(0,0,0,.18);overflow:hidden}
.photo{position:absolute}
.brand{position:absolute;display:flex;align-items:center;gap:8px;font-family:'Lexend',sans-serif;font-weight:400;color:var(--dark)}
.brand .dot{width:14px;height:14px;border-radius:50%;background:var(--orange)}
/* header */
.slide-header{position:absolute;left:0;top:0;width:1048px;height:96px}
.slide-header svg{position:absolute;left:0;top:0}
.slide-title{position:absolute;left:60px;top:22px;font-family:'Lexend',sans-serif;font-weight:500;font-size:34px;color:var(--white);letter-spacing:-.5px}
.header-brand{right:60px;top:30px;font-size:24px}
/* cover */
.cover-photo{left:0;top:0;width:1048px;height:440px;background:linear-gradient(135deg,#1b2d48 0%,#2f5580 45%,#8fb1d6 100%)}
.cover-brand{left:205px;top:492px;font-size:30px}
.cover-divider{position:absolute;left:400px;top:468px;width:2px;height:72px;background:#dfe3e4}
.cover-title{position:absolute;left:453px;top:470px;font-family:'Lexend',sans-serif;font-size:34px;font-weight:400;color:var(--orange)}
.cover-tagline{position:absolute;left:453px;top:525px;font-size:17px;color:var(--dark)}
/* about */
.body-copy{position:absolute;font-size:13px;line-height:24.5px;text-align:justify;color:var(--text)}
.about-copy{left:61px;top:180px;width:411px}
.about-small-a{left:61px;top:351px;width:219px;height:174px;background:linear-gradient(135deg,#0e2a3a,#2b7c90)}
.about-small-b{left:292px;top:351px;width:219px;height:174px;background:linear-gradient(135deg,#1b2236,#3e5f8c)}
.about-large{left:524px;top:153px;width:464px;height:372px;background:linear-gradient(135deg,#c9ccd0 0%,#3d5066 45%,#0f2235 100%)}
/* solutions */
.solutions-map{position:absolute;left:0;top:0}
.sol-label{position:absolute;font-size:12px;font-weight:700;color:var(--dark);line-height:18px;text-transform:uppercase}
.sol-label.left{text-align:right;width:220px}
.sol-label.top{left:424px;width:200px;text-align:center;top:126px}
/* why */
.why-photo{left:61px;top:156px;width:463px;height:372px;background:linear-gradient(120deg,#2b2f33 0%,#7a8a85 40%,#dfe4e2 100%)}
.why-accent{position:absolute;left:0;top:266px;width:12px;height:151px;background:var(--orange)}
.why-copy{left:577px;top:244px;width:411px;font-size:12.5px}
/* partners */
.partner-card{position:absolute;width:219px;height:102px;background:var(--white);border-radius:4px;box-shadow:0 3px 12px rgba(0,0,0,.22);display:flex;align-items:center;justify-content:center}
.partner-badge{width:128px;height:34px;border-radius:6px;background:#e3e7ea}
/* closing */
.closing-panel{position:absolute;left:0;top:0;width:387px;height:588px;background:linear-gradient(160deg,#2d3638,#242b2d)}
.closing-rule{position:absolute;left:387px;top:0;width:4px;height:588px;background:var(--blue)}
.closing-photo{left:391px;top:0;width:657px;height:588px;background:linear-gradient(135deg,#1a2540 0%,#3b5d93 50%,#8fa8cf 100%)}
.closing-brand{left:61px;top:40px;font-size:26px;color:var(--white)}
.thanks{position:absolute;left:61px;top:196px;font-family:'Lexend',sans-serif;font-weight:500;font-size:50px;color:var(--white);letter-spacing:-1px}
.thanks span{color:var(--orange)}
.contact{position:absolute;left:61px;display:flex;align-items:center;gap:28px;font-size:16px;color:var(--white)}
.contact svg{width:32px;height:26px}
.socials{position:absolute;left:61px;top:536px;display:flex;gap:9px}
.socials span{width:28px;height:28px;border:1.5px solid var(--white);border-radius:50%}
</style>
</head>
<body>

<!-- Cover -->
<section class="slide" style="top:88px">
  <div class="photo cover-photo" role="img" aria-label="Photo of two engineers with a laptop in a server room"></div>
  <div class="brand cover-brand"><span class="dot"></span>Brovana</div>
  <div class="cover-divider"></div>
  <div class="cover-title">Brovana</div>
  <div class="cover-tagline">A Clear Path to IT Optimization</div>
</section>

<!-- About -->
<section class="slide" style="top:747px">
  <div class="slide-header">
    <svg width="1048" height="96" viewBox="0 0 1048 96">
      <rect x="0" y="0" width="1048" height="5" fill="#2c3536"/>
      <polygon points="0,0 700,0 630,92 0,92" fill="#3e9c78"/>
      <polygon points="0,0 690,0 622,86 0,86" fill="#2c3536"/>
    </svg>
    <div class="slide-title">About Us</div>
    <div class="brand header-brand"><span class="dot"></span>Brovana</div>
  </div>
  <p class="body-copy about-copy">In a complex world of IT Brovana will assist you in optimizing IT spend. Our 20 plus years in the IT industry brings best of breed personnel from Data center, Managed Services, and Disaster Recovery, to help you get the best solutions for the best price. In a complex world of IT, let us help simplify.</p>
  <div class="photo about-small-a" role="img" aria-label="Photo of hands typing on a laptop with glowing data graphics"></div>
  <div class="photo about-small-b" role="img" aria-label="Photo of a team working at screens in a dark office"></div>
  <div class="photo about-large" role="img" aria-label="Photo of a hand touching a network of digital icons above a laptop"></div>
</section>

<!-- Solutions -->
<section class="slide" style="top:1406px">
  <div class="slide-header">
    <svg width="1048" height="96" viewBox="0 0 1048 96">
      <rect x="0" y="0" width="1048" height="5" fill="#2c3536"/>
      <polygon points="0,0 700,0 630,92 0,92" fill="#3e9c78"/>
      <polygon points="0,0 690,0 622,86 0,86" fill="#2c3536"/>
    </svg>
    <div class="slide-title">Our Solutions</div>
    <div class="brand header-brand"><span class="dot"></span>Brovana</div>
  </div>
  <svg class="solutions-map" width="1048" height="588" viewBox="0 0 1048 588">
    <g fill="none" stroke="#1f7fcf" stroke-width="1.6">
      <circle cx="524" cy="407" r="131"/>
      <line x1="524" y1="276" x2="524" y2="243"/>
      <polyline points="408,342 376,306 331,306"/>
      <line x1="392" y1="407" x2="331" y2="407"/>
      <polyline points="408,472 376,507 331,507"/>
      <polyline points="640,342 672,306 717,306"/>
      <line x1="656" y1="407" x2="717" y2="407"/>
      <polyline points="640,472 672,507 717,507"/>
    </g>
    <g fill="#fff" stroke="#1f7fcf" stroke-width="2">
      <circle cx="524" cy="276" r="5"/>
      <circle cx="408" cy="342" r="5"/><circle cx="392" cy="407" r="5"/><circle cx="408" cy="472" r="5"/>
      <circle cx="640" cy="342" r="5"/><circle cx="656" cy="407" r="5"/><circle cx="640" cy="472" r="5"/>
    </g>
    <circle cx="524" cy="407" r="110" fill="#2c3536"/>
    <circle cx="496" cy="407" r="10" fill="#dd6a1d"/>
    <text x="530" y="414" fill="#fff" font-family="Lexend, sans-serif" font-size="30" text-anchor="middle">   Brovana</text>
    <g>
      <g transform="translate(524,203)"><circle r="40" fill="#fff" stroke="#e3e6e8" stroke-width="2"/><circle r="34" fill="#dd6a1d"/><path d="M-10,-4 A11,11 0 1 1 -6,9 M-10,-4 L-12,-12 M-10,-4 L-2,-6" fill="none" stroke="#fff" stroke-width="2.2"/></g>
      <g transform="translate(291,306)"><circle r="40" fill="#fff" stroke="#e3e6e8" stroke-width="2"/><circle r="34" fill="#dd6a1d"/><rect x="-13" y="-11" width="26" height="20" rx="2" fill="none" stroke="#fff" stroke-width="2.2"/><path d="M-8,5 L-3,-2 L2,3 L8,-5" fill="none" stroke="#fff" stroke-width="2"/></g>
      <g transform="translate(291,407)"><circle r="40" fill="#fff" stroke="#e3e6e8" stroke-width="2"/><circle r="34" fill="#dd6a1d"/><g fill="none" stroke="#fff" stroke-width="2.2"><rect x="-6" y="-14" width="12" height="8"/><rect x="-15" y="5" width="9" height="8"/><rect x="-4" y="5" width="9" height="8"/><rect x="7" y="5" width="9" height="8"/><path d="M0,-6 V0 M-11,5 V0 H11 V5 M0,0 V5"/></g></g>
      <g transform="translate(291,507)"><circle r="40" fill="#fff" stroke="#e3e6e8" stroke-width="2"/><circle r="34" fill="#dd6a1d"/><path d="M-12,4 A7,7 0 0 1 -8,-7 A9,9 0 0 1 9,-6 A6,6 0 0 1 12,4 Z M-6,8 H6 M-6,12 H6" fill="none" stroke="#fff" stroke-width="2.2"/></g>
      <g transform="translate(757,306)"><circle r="40" fill="#fff" stroke="#e3e6e8" stroke-width="2"/><circle r="34" fill="#dd6a1d"/><rect x="-13" y="-11" width="26" height="20" rx="2" fill="none" stroke="#fff" stroke-width="2.2"/><circle cx="3" cy="0" r="6" fill="none" stroke="#fff" stroke-width="2"/><path d="M7,4 L13,10" stroke="#fff" stroke-width="2.2"/></g>
      <g transform="translate(757,407)"><circle r="40" fill="#fff" stroke="#e3e6e8" stroke-width="2"/><circle r="34" fill="#dd6a1d"/><g fill="none" stroke="#fff" stroke-width="2.2"><rect x="-13" y="-12" width="26" height="7" rx="2"/><rect x="-13" y="-3" width="26" height="7" rx="2"/><rect x="-13" y="6" width="26" height="7" rx="2"/></g></g>
      <g transform="translate(757,507)"><circle r="40" fill="#fff" stroke="#e3e6e8" stroke-width="2"/><circle r="34" fill="#dd6a1d"/><path d="M0,-13 L11,-8 V1 C11,8 5,12 0,14 C-5,12 -11,8 -11,1 V-8 Z M-5,0 L-1,5 L6,-4" fill="none" stroke="#fff" stroke-width="2.2"/></g>
    </g>
  </svg>
  <div class="sol-label top">Disaster Recovery</div>
  <div class="sol-label left" style="left:8px;top:297px">Midrange/Unix Systems</div>
  <div class="sol-label left" style="left:8px;top:398px">Mainframe</div>
  <div class="sol-label left" style="left:8px;top:498px">Cloud</div>
  <div class="sol-label" style="left:818px;top:288px">IT Optimization<br>Strategies</div>
  <div class="sol-label" style="left:818px;top:398px">Colocation</div>
  <div class="sol-label" style="left:818px;top:498px">Security</div>
</section>

<!-- Why -->
<section class="slide" style="top:2065px">
  <div class="slide-header">
    <svg width="1048" height="96" viewBox="0 0 1048 96">
      <rect x="0" y="0" width="1048" height="5" fill="#2c3536"/>
      <polygon points="0,0 700,0 630,92 0,92" fill="#3e9c78"/>
      <polygon points="0,0 690,0 622,86 0,86" fill="#2c3536"/>
    </svg>
    <div class="slide-title">Why Brovana ?</div>
    <div class="brand header-brand"><span class="dot"></span>Brovana</div>
  </div>
  <div class="why-accent"></div>
  <div class="photo why-photo" role="img" aria-label="Photo of two colleagues with a laptop beside server racks"></div>
  <p class="body-copy why-copy">It's Simple. Our resources have years of experience understanding IT environments. All of our staff have been top of their class in each of their specialties and can help you optimize your spend with best of breed solutioning. Our staff have unmatched knowledge in Networking, Security, Data Center, Disaster Recovery, Titanline Solutions, Hyperscaler Solutions, Managed Services, and more. The people we put in front of you are the best of the best in IT. Let our team help you optimize your environment.</p>
</section>

<!-- Partners -->
<section class="slide" style="top:2724px">
  <div class="slide-header">
    <svg width="1048" height="96" viewBox="0 0 1048 96">
      <rect x="0" y="0" width="1048" height="5" fill="#2c3536"/>
      <polygon points="0,0 700,0 630,92 0,92" fill="#3e9c78"/>
      <polygon points="0,0 690,0 622,86 0,86" fill="#2c3536"/>
    </svg>
    <div class="slide-title">OUR PARTNERS</div>
    <div class="brand header-brand"><span class="dot"></span>Brovana</div>
  </div>
  <div class="partner-card" style="left:159px;top:217px"><div class="partner-badge" role="img" aria-label="Partner badge"></div></div>
  <div class="partner-card" style="left:415px;top:217px"><div class="partner-badge" role="img" aria-label="Partner badge"></div></div>
  <div class="partner-card" style="left:670px;top:217px"><div class="partner-badge" role="img" aria-label="Partner badge"></div></div>
  <div class="partner-card" style="left:288px;top:365px"><div class="partner-badge" role="img" aria-label="Partner badge"></div></div>
  <div class="partner-card" style="left:543px;top:365px"><div class="partner-badge" role="img" aria-label="Partner badge"></div></div>
</section>

<!-- Closing -->
<section class="slide" style="top:3383px">
  <div class="closing-panel"></div>
  <div class="closing-rule"></div>
  <div class="photo closing-photo" role="img" aria-label="Photo of two engineers with a laptop in a blue-lit data center"></div>
  <div class="brand closing-brand"><span class="dot"></span>Brovana</div>
  <div class="thanks">Thank <span>You</span></div>
  <div class="contact" style="top:302px">
    <svg viewBox="0 0 32 26"><path d="M6,3 L11,3 L13,9 L10,11 C12,15 15,18 19,20 L21,17 L27,19 L27,24 C16,24 6,14 6,3 Z" fill="none" stroke="#fff" stroke-width="2"/><path d="M18,3 A8,8 0 0 1 26,11 M18,7 A4,4 0 0 1 22,11" fill="none" stroke="#fff" stroke-width="1.8"/></svg>
    <span>+1 (555) 014 2270</span>
  </div>
  <div class="contact" style="top:355px">
    <svg viewBox="0 0 32 26"><g fill="none" stroke="#fff" stroke-width="1.8"><circle cx="16" cy="13" r="11"/><ellipse cx="16" cy="13" rx="5" ry="11"/><path d="M5,13 H27 M7,7 H25 M7,19 H25"/></g></svg>
    <span>https://brovana.info/</span>
  </div>
  <div class="contact" style="top:409px">
    <svg viewBox="0 0 32 26"><g fill="none" stroke="#fff" stroke-width="2"><rect x="3" y="4" width="26" height="18"/><path d="M3,4 L16,15 L29,4 M3,22 L12,12 M29,22 L20,12"/></g></svg>
    <span>info@brovana.info</span>
  </div>
  <div class="socials"><span></span><span></span><span></span><span></span><span></span></div>
</section>

</body>
</html>
```